Chiropractic healthcare group business card

We are a Portland Oregon based chiropractic healthcare group. Looking for a new business card design. Something cutting edge, that shows off our new logo and tag line.Use either of the attached logos.Our tag line = "Who would you be without pain?"I'm open to about anything, impress me!!
Target Market(s)
Chiropractic patients - Auto injury, back pain, sports injuries, neck , shoulder, hip, knee, ankle pain.
Industry/Entity Type
Chiropractic
Contact Information for Business Card
Dr. Bram Holtvick, D.C.
Clinic name - Fernway Chiropractic
2 clinics
location #1
20418 NW Marwick Road
Suite B
North Plains, OR 97133
Location #2
13529 SE Calloway Street
Portland OR 97236
Main phone line 971.555.0143
website : www.FernwayClinics.example
Tag line "Who would you be without pain?"
Colors
Designer to choose colors to be used in the design.
Requirements
Must have
- Use the logo colors -- Want the orange color to be a TRUE orange.
- Both clinic address
- phone number
- website
- personal email - b.holtvick@ReliefBeginsHere.example
- tag line - "Who would you be without pain?"

```html
<!DOCTYPE html>
<html lang="en">
<head>
<meta charset="UTF-8">
<title>Bram Holtvick – Fernway Chiropractic Business Card</title>
<link rel="stylesheet" href="https://fonts.googleapis.com/css2?family=Lora:wght@700&family=Dosis:wght@400;500&display=swap">
<style>
  :root {
    --cream: #fcf9e6;
    --orange: #f7a42b;
    --white: #fffdf5;
    --ink-grey: #77736c;
  }
  html, body {
    margin: 0;
    padding: 0;
    width: 1200px;
    height: 707px;
    overflow: hidden;
    background: var(--cream);
  }
  .card {
    position: relative;
    width: 1200px;
    height: 707px;
    background: var(--cream);
  }
  .card__name {
    position: absolute;
    top: 162px;
    left: 0;
    width: 100%;
    margin: 0;
    text-align: center;
    font-family: "Lora", serif;
    font-weight: 700;
    font-size: 58px;
    line-height: 70px;
    letter-spacing: 0.18em;
    text-indent: 0.18em;
    color: var(--orange);
    text-transform: uppercase;
    white-space: nowrap;
  }
  .card__band {
    position: absolute;
    top: 270px;
    left: 0;
    width: 100%;
    height: 89px;
    background: var(--orange);
    display: flex;
    align-items: center;
    justify-content: center;
  }
  .card__clinic {
    margin: 0;
    font-family: "Dosis", sans-serif;
    font-weight: 500;
    font-size: 38px;
    letter-spacing: 0.22em;
    text-indent: 0.22em;
    color: var(--white);
    text-transform: uppercase;
    white-space: nowrap;
  }
  .card__contact {
    position: absolute;
    top: 384px;
    left: 0;
    width: 100%;
    margin: 0;
    padding: 0;
    list-style: none;
    text-align: center;
    font-family: "Dosis", sans-serif;
    font-weight: 500;
    font-size: 27px;
    line-height: 40px;
    letter-spacing: 0.08em;
    color: var(--ink-grey);
    white-space: nowrap;
  }
  .card__tagline {
    position: absolute;
    top: 630px;
    left: 0;
    width: 100%;
    margin: 0;
    text-align: center;
    font-family: "Dosis", sans-serif;
    font-weight: 500;
    font-size: 27px;
    line-height: 40px;
    letter-spacing: 0.08em;
    color: var(--orange);
  }
</style>
</head>
<body>
  <main class="card">
    <h1 class="card__name">Bram Holtvick, D.C.</h1>
    <div class="card__band">
      <p class="card__clinic">Fernway Chiropractic</p>
    </div>
    <ul class="card__contact">
      <li>Phone: 971.555.0143</li>
      <li>20418 NW Marwick Road, Suite B, North Plains, OR 97133</li>
      <li>13529 SE Calloway Street, Portland, OR 97236</li>
      <li>Email: b.holtvick@ReliefBeginsHere.example</li>
      <li>Website: www.FernwayClinics.example</li>
    </ul>
    <p class="card__tagline">Who would you be without pain?</p>
  </main>
</body>
</html>
```